KVRD Pinecrest Rehabilitation Consultants, INC
Business Card and Stationary for KVRD Pinecrest Rehabilitation
Professional
Dorian K. Lumbard, Ph. D.
Vocational Rehabilitation Consultant
4173b GA Hwy 508 STE 612 Conyers, GA 30081
Dorian.Lumbard@kvrdpinecrestrehab.example
www.kvrdpinecrestrehab.example
I will need whole set of stationary, letterhead, envelopes etc.

```html
<!DOCTYPE html>
<html lang="en">
<head>
<meta charset="utf-8">
<title>KVRD Pinecrest Rehabilitation – Business Card</title>
<link href="https://fonts.googleapis.com/css2?family=Cinzel:wght@500&family=Open+Sans:wght@400;600&display=swap" rel="stylesheet">
<style>
  :root{
    --page:#e9ebee;
    --card:#ffffff;
    --blue-deep:#0b4fb8;
    --blue-mid:#1f7de0;
    --blue-light:#5fb4f5;
    --swoosh:#3a3d44;
    --ink-blue:#1760c4;
    --ink-grey:#5d6068;
    --on-blue:#ffffff;
  }
  html,body{margin:0;padding:0;width:1200px;height:901px;overflow:hidden;background:var(--page);}
  .card{
    position:absolute;left:150px;top:190px;width:900px;height:520px;
    background:var(--card);border-radius:40px;overflow:hidden;
    box-shadow:0 14px 40px rgba(0,0,0,.18);
    font-family:"Open Sans",sans-serif;
  }
  .card-waves{position:absolute;inset:0;}
  .brand{position:absolute;left:60px;top:60px;display:flex;align-items:center;gap:18px;}
  .brand-dot{width:58px;height:58px;border-radius:50%;background:var(--ink-blue);}
  .brand-name{font-family:"Cinzel",serif;font-weight:500;color:var(--ink-blue);font-size:54px;letter-spacing:4px;line-height:1;}
  .brand-sub{font-family:"Cinzel",serif;font-weight:500;color:var(--ink-blue);font-size:14px;letter-spacing:3px;margin-top:6px;}
  .holder{position:absolute;right:60px;top:95px;text-align:right;}
  .holder-name{color:var(--ink-blue);font-size:26px;font-weight:600;letter-spacing:1px;margin:0;}
  .holder-title{color:var(--ink-grey);font-size:17px;margin:4px 0 0;}
  .contact{position:absolute;right:60px;top:330px;list-style:none;margin:0;padding:0;color:var(--on-blue);font-size:15px;line-height:1.95;}
  .contact li{display:flex;align-items:center;justify-content:flex-end;gap:10px;}
  .contact svg{width:14px;height:14px;fill:var(--on-blue);}
</style>
</head>
<body>
<section class="card">
  <svg class="card-waves" viewBox="0 0 900 520" preserveAspectRatio="none">
    <defs>
      <linearGradient id="blueBand" x1="0" y1="0" x2="1" y2="1">
        <stop offset="0" stop-color="var(--blue-light)"/>
        <stop offset=".45" stop-color="var(--blue-mid)"/>
        <stop offset="1" stop-color="var(--blue-deep)"/>
      </linearGradient>
    </defs>
    <path d="M0,238 C230,170 470,350 900,250 L900,275 C470,380 230,200 0,262 Z" fill="var(--swoosh)"/>
    <path d="M0,268 C240,210 460,390 900,290 L900,520 L0,520 Z" fill="url(#blueBand)"/>
  </svg>

  <div class="brand">
    <span class="brand-dot"></span>
    <div>
      <div class="brand-name">KVRD</div>
      <div class="brand-sub">PINECREST REHABILITATION</div>
    </div>
  </div>

  <div class="holder">
    <p class="holder-name">DORIAN K. LUMBARD, PH. D.</p>
    <p class="holder-title">Vocational Rehabilitation Consultant</p>
  </div>

  <ul class="contact">
    <li>4173b GA Hwy 508 STE 612 Conyers, GA 30081
      <svg viewBox="0 0 24 24"><path d="M12 2a7 7 0 0 0-7 7c0 5 7 13 7 13s7-8 7-13a7 7 0 0 0-7-7zm0 9.5A2.5 2.5 0 1 1 12 6.5a2.5 2.5 0 0 1 0 5z"/></svg></li>
    <li>Tel 555 014 2290
      <svg viewBox="0 0 24 24"><path d="M6.6 10.8a15 15 0 0 0 6.6 6.6l2.2-2.2a1 1 0 0 1 1-.25 11 11 0 0 0 3.6.6 1 1 0 0 1 1 1V20a1 1 0 0 1-1 1A17 17 0 0 1 3 4a1 1 0 0 1 1-1h3.5a1 1 0 0 1 1 1 11 11 0 0 0 .6 3.6 1 1 0 0 1-.25 1z"/></svg></li>
    <li>Fax 555 014 2291
      <svg viewBox="0 0 24 24"><rect x="4" y="8" width="16" height="10" rx="2"/><rect x="7" y="3" width="10" height="5"/></svg></li>
    <li>Dorian.Lumbard@kvrdpinecrestrehab.example
      <svg viewBox="0 0 24 24"><path d="M3 5h18v14H3z M3 5l9 7 9-7" fill="none" stroke="#fff" stroke-width="2"/></svg></li>
    <li>www.kvrdpinecrestrehab.example
      <svg viewBox="0 0 24 24"><circle cx="12" cy="12" r="9" fill="none" stroke="#fff" stroke-width="2"/><path d="M3 12h18M12 3c3 3 3 15 0 18M12 3c-3 3-3 15 0 18" fill="none" stroke="#fff" stroke-width="1.5"/></svg></li>
  </ul>
</section>
</body>
</html>
```